Hadwick Zephra Jet - Redefining Clean.

I am looking for an elegant, modern brochure design that will convey our high end and luxury product.

Hadwick Group was established in 1960. It began as a small logging company and has since branched out with divisions working in the aviation, logging, lumber manufacturing, and gaming industries. Our most recent venture has been the establishment of our Zephra Jet division.

Zephra Jet is not a new technology and is much different than dry ice. The company that invented the technology and built the original Zephra Jet machines had been around for twenty years before the Hadwick Group acquired the technology and patents.
The previous incarnation of Zephra Jet had machines located all over the world in the nuclear, marine, oil & gas, automotive and restoration sectors. As with everything we do, we strive for excellence. So we took the previous models of the Zephra Jet and re-engineered the technology to make it better and even more effective. Two years later we have created an environmentally friendly and superior cleaning technology that is ready to go to market.

Please note that currently there is minimal information regarding our product and zephra jet division on the web as we have not launched the company yet.

I have attached some information to further help you come up with some concepts.

File #1 - Our Logo
File #2 - Some information on our technology
File #3 - Some information on our technology
File #4 - A high rez picture of the product
File #5 - A brochure we really like the look of
File #6 - A brochure we really like the look of
File #7 - A picture of our website home page

Kind Regards,

Milo Hadwick

Target Market(s)

Environmental cleaning applications

Industry/Entity Type

Automotive

Contact Information for Business Card

Milo Hadwick - Hadwick Zephra Jet - Office number 250.555.0193 - Email - Milo.hadwick@hadwickgroup-mail.com

Font styles to use
Other font styles liked:
• Similar to logo font.

Requirements
Must have
• I am looking for a multi page, modern design that is similar to the brochures attached.
• Letter font similar to Logo
• Incorporate our slogan - 'Redefining clean'
Nice to have
• Creative
• It would be very interesting to see a design similar to my attached file #5 but instead of the square cut outs on the cover, there is a cut out of the Zephra Jet Logo.

```html
<!DOCTYPE html>
<html lang="en">
<head>
<meta charset="utf-8">
<title>Hadwick Zephra Jet – Technology Spread</title>
<link rel="stylesheet" href="https://fonts.googleapis.com/css2?family=Questrial&family=Arimo:wght@400;700&display=swap">
<style>
  :root {
    --page-bg: #e9e6e1;
    --panel-blue: rgba(52, 124, 190, 0.88);
    --photo-dark: #2f3133;
    --photo-mid: #6d7174;
    --photo-light: #a9adb0;
    --edge-dark: #3a3d3f;
    --ink-dark: #1f2326;
    --ink-white: #ffffff;
    --subhead: #e3eefa;
    --frame: #2b2d2f;
    --frame-inner: #ffffff;
  }
  * { box-sizing: border-box; margin: 0; padding: 0; }
  html, body {
    width: 1200px; height: 595px; overflow: hidden;
    background: var(--page-bg);
  }
  .spread {
    position: absolute; left: 32px; top: 30px;
    width: 1136px; height: 537px; overflow: hidden;
  }
  .spread-photo {
    position: absolute; inset: 0;
    background:
      linear-gradient(90deg, var(--photo-dark) 0%, var(--photo-mid) 18%, var(--photo-light) 32%, var(--photo-mid) 40%, var(--photo-dark) 48%, var(--photo-light) 60%, var(--photo-mid) 68%, var(--photo-dark) 80%, var(--photo-mid) 100%);
  }
  .spread-edge {
    position: absolute; top: 0; right: 0; width: 63px; height: 100%;
    background: var(--edge-dark);
  }
  .panel {
    position: absolute; top: 0; height: 100%;
    background: var(--panel-blue);
  }
  .panel--left { left: 78px; width: 348px; }
  .panel--right { left: 716px; width: 357px; }
  .panel-title {
    font-family: "Questrial", sans-serif; font-weight: 400;
    font-size: 31px; line-height: 36px; letter-spacing: 0.3px;
  }
  .panel--left .panel-title {
    position: absolute; left: 27px; top: 36px; width: 320px;
    color: var(--ink-dark);
  }
  .panel--right .panel-title {
    position: absolute; left: 0; top: 36px; width: 100%;
    color: var(--ink-white); text-align: center;
  }
  .panel-subtitle {
    position: absolute; left: 65px; top: 114px; width: 228px;
    font-family: "Arimo", sans-serif; font-size: 12.5px; letter-spacing: 0.6px;
    color: var(--subhead); text-align: center;
    padding-bottom: 3px; border-bottom: 1.5px solid var(--subhead);
  }
  .panel-body {
    position: absolute; font-family: "Arimo", sans-serif; font-weight: 700;
    font-size: 12.5px; line-height: 22px; letter-spacing: 0.9px;
    text-align: justify; text-align-last: left;
  }
  .panel--left .panel-body { left: 38px; top: 141px; width: 266px; color: var(--ink-white); }
  .panel--right .panel-body { left: 47px; top: 140px; width: 265px; color: var(--ink-dark); }
  .diagram-frame {
    position: absolute; background: var(--frame);
    border-radius: 3px; padding: 9px;
  }
  .panel--left .diagram-frame { left: 52px; top: 270px; width: 226px; height: 170px; }
  .panel--right .diagram-frame { left: 65px; top: 263px; width: 228px; height: 168px; }
  .diagram {
    width: 100%; height: 100%; background: var(--frame-inner);
    box-shadow: inset 0 0 10px rgba(0,0,0,0.25);
  }
  .diagram--nozzle {
    background: radial-gradient(ellipse at 55% 45%, #c9d6d8 0%, #e6d6c8 35%, #ffffff 70%);
  }
  .diagram--removal {
    background: linear-gradient(180deg, #ffffff 0%, #ffffff 55%, #f1dcc0 75%, #ffffff 100%);
  }
</style>
</head>
<body>
  <main class="spread">
    <div class="spread-photo" role="img" aria-label="Photograph of the Zephra Jet machine cabinet with perforated hexagon mesh doors"></div>
    <div class="spread-edge"></div>

    <section class="panel panel--left">
      <h1 class="panel-title">Zephra Jet Technology</h1>
      <p class="panel-body">In Zephra Jet Technology , the Fractured Ice Chips are Continuously Suctioned away to a blast nozzle , then Propelled Towards a Work Piece .</p>
      <div class="diagram-frame">
        <div class="diagram diagram--nozzle" role="img" aria-label="Illustration of the ice drum feeding fractured chips through a hose to the blast nozzle"></div>
      </div>
    </section>

    <section class="panel panel--right">
      <h2 class="panel-title">Zephra Jet Cleaning<br>Mechanism</h2>
      <p class="panel-subtitle">Displacement Work (Bulk Removal)</p>
      <p class="panel-body">Under Proper Conditions of Drum Diameter, Temperature, Ice Thickness and Rotational Speed , the Formed Ice Sheet has Sufficient Internal Stress to Self-Fracture</p>
      <div class="diagram-frame">
        <div class="diagram diagram--removal" role="img" aria-label="Illustration of an ice particle striking a surface and lifting contaminant flakes away"></div>
      </div>
    </section>
  </main>
</body>
</html>
```